Business Cards for a law firm

Business cards for our law firm. Use our silhoette logo and OAK HARBOR - check our website (www.oakharbor-legal.com)

Contact Information for Business Card

our silhouette logo, OAK HARBOR, 800-555-0147, Dorian Kestrup, dorian@oakharbor-legal.com

Requirements
Must have
• our silhouette logo, OAK HARBOR, 800-555-0147, Dorian Kestrup, dorian@oakharbor-legal.com

```html
<!DOCTYPE html>
<html lang="en">
<head>
<meta charset="utf-8">
<title>Oak Harbor – Business Cards</title>
<link rel="stylesheet" href="https://fonts.googleapis.com/css2?family=Saira:wght@600;700&family=Nunito+Sans:wght@400&display=swap">
<style>
  :root {
    --navy: #22336c;
    --ink: #1f2230;
    --paper: #ffffff;
    --backdrop: #e6e7ea;
  }
  * { margin: 0; padding: 0; box-sizing: border-box; }
  html, body { width: 1200px; height: 1059px; overflow: hidden; }
  body { background: var(--backdrop); position: relative; font-family: "Nunito Sans", sans-serif; color: var(--ink); }

  .card { position: absolute; overflow: hidden; }
  .card-front { left: 256px; top: 100px; width: 688px; height: 391px; background: var(--paper); }
  .card-back { left: 253px; top: 537px; width: 694px; height: 394px; background: var(--navy); }

  .brand { position: absolute; display: flex; align-items: center; font-family: "Saira", sans-serif; font-weight: 700; letter-spacing: 1px; white-space: nowrap; }
  .brand-mark { display: inline-block; background: currentColor; }
  .card-front .brand { right: 39px; top: 56px; color: var(--navy); font-size: 32px; gap: 12px; }
  .card-front .brand-mark { width: 22px; height: 22px; }
  .card-back .brand { left: 0; right: 0; top: 160px; justify-content: center; color: var(--paper); font-size: 50px; gap: 18px; }
  .card-back .brand-mark { width: 34px; height: 34px; }

  .name-tab { position: absolute; left: 0; top: 198px; width: 19px; height: 41px; background: var(--navy); border-radius: 0 4px 4px 0; }
  .person-name { position: absolute; left: 39px; top: 192px; font-family: "Saira", sans-serif; font-weight: 600; font-size: 26px; line-height: 32px; color: var(--navy); letter-spacing: 0.3px; }
  .person-role { position: absolute; left: 39px; top: 225px; font-size: 15px; letter-spacing: 0.5px; }
  .divider { position: absolute; left: 39px; top: 259px; width: 610px; height: 2px; background: var(--navy); }

  .contact-list { position: absolute; left: 39px; top: 281px; list-style: none; }
  .contact-list li { display: flex; align-items: center; height: 26px; font-size: 16px; }
  .contact-list svg { width: 14px; height: 14px; margin-right: 10px; fill: var(--navy); flex: none; }

  .address { position: absolute; right: 39px; top: 312px; text-align: right; font-size: 16px; line-height: 20px; font-style: normal; }
</style>
</head>
<body>
  <section class="card card-front">
    <div class="brand"><span class="brand-mark"></span>OAK HARBOR</div>
    <div class="name-tab"></div>
    <h1 class="person-name">DORIAN KESTRUP</h1>
    <p class="person-role">OWNER</p>
    <div class="divider"></div>
    <ul class="contact-list">
      <li><svg viewBox="0 0 24 24"><path d="M6.6 10.8a15.1 15.1 0 0 0 6.6 6.6l2.2-2.2c.3-.3.7-.4 1-.2 1.1.4 2.3.6 3.6.6.6 0 1 .4 1 1V20c0 .6-.4 1-1 1A17 17 0 0 1 3 4c0-.6.4-1 1-1h3.5c.6 0 1 .4 1 1 0 1.3.2 2.5.6 3.6.1.3 0 .7-.2 1z"/></svg>800-555-0147</li>
      <li><svg viewBox="0 0 24 24"><path d="M2 4h20v16H2zm2 3v11h16V7l-8 6z"/></svg>dorian@oakharbor-legal.com</li>
      <li><svg viewBox="0 0 24 24"><path d="M12 2a10 10 0 1 0 0 20 10 10 0 0 0 0-20zm-1 17.9A8 8 0 0 1 4.2 10L9 14.8v1a2 2 0 0 0 2 2zm6.9-2.5a2 2 0 0 0-1.9-1.4h-1v-3a1 1 0 0 0-1-1H8v-2h2a1 1 0 0 0 1-1V7h2a2 2 0 0 0 2-2v-.4a8 8 0 0 1 2.9 12.8z"/></svg>www.oakharbor-legal.com</li>
    </ul>
    <address class="address">4120 Harbor View Ave #310,<br>Seaport City, CA 90000</address>
  </section>

  <section class="card card-back">
    <div class="brand"><span class="brand-mark"></span>OAK HARBOR</div>
  </section>
</body>
</html>
```